Calibrated NET Systems
Business card and Stationary
Project: Calibrated NET Systems
Calibrated NET Systems - Information Technology
Creative Brief
Professional
Dean Harlowe
Technical Consultant
Please leave the address part blank.
dean.harlowe@calnet.ca
www.calnet.ca

```html
<!DOCTYPE html>
<html lang="en">
<head>
<meta charset="utf-8">
<title>Calibrated NET Systems – Stationery</title>
<link rel="stylesheet" href="https://fonts.googleapis.com/css2?family=Montserrat:wght@400;600&display=swap">
<style>
:root{
  --bg:#e9e4dc;
  --paper:#ffffff;
  --blue:#1b8ad3;
  --blue-dark:#0d5f9e;
  --ink:#3a3a3a;
  --muted:#8a8a8a;
  --rule:#9a9a9a;
  --label:#4a4036;
}
*{box-sizing:border-box;margin:0;padding:0}
html,body{width:1200px;height:559px;overflow:hidden}
body{background:var(--bg);font-family:"Montserrat",Arial,sans-serif;color:var(--ink);position:relative}
.piece{position:absolute;background:var(--paper);box-shadow:0 2px 6px rgba(0,0,0,.25)}
.piece-label{position:absolute;font-size:8px;font-weight:600;color:var(--label);text-align:center;width:100%;top:-12px;left:0}
.brand{position:absolute;display:flex;align-items:center;gap:5px;color:var(--blue);font-weight:600;white-space:nowrap}
.brand-mark{background:var(--blue);display:block}
.contact{position:absolute;list-style:none;font-size:5px;line-height:8px;color:var(--ink)}
.contact li{display:flex;align-items:center;gap:3px}
.contact li::before{content:"";width:4px;height:4px;border-radius:50%;background:var(--blue)}

/* sheets */
.fax-sheet{left:36px;top:19px;width:348px;height:521px}
.letterhead{left:408px;top:19px;width:348px;height:521px}
.sheet-brand{left:18px;top:20px;font-size:15px}
.sheet-brand .brand-mark{width:18px;height:18px}
.sheet-contact{left:226px;top:14px}
.fax-title{position:absolute;right:20px;top:70px;font-size:12px;font-weight:600;letter-spacing:1px}
.fax-table{position:absolute;left:18px;top:86px;width:312px;border-collapse:collapse;font-size:6px}
.fax-table td{border:1px solid var(--rule);height:19px;padding:0 4px;width:25%}
.fax-table td.field{width:30%}
.fax-table td.key{width:20%}
.fax-checks{position:absolute;left:18px;top:172px;display:flex;gap:14px;font-size:5.5px}
.fax-checks span{display:flex;align-items:center;gap:3px}
.fax-checks span::before{content:"";width:5px;height:5px;border:1px solid var(--rule)}

/* cards */
.card{top:29px;width:172px;height:86px}
.card-front{left:780px;overflow:hidden}
.card-back{left:960px;border-radius:6px;display:flex;align-items:center;justify-content:center}
.card-swoosh{position:absolute;left:0;top:0}
.card-name{position:absolute;right:10px;top:14px;text-align:right;font-size:6px;color:#fff;font-weight:600}
.card-name small{display:block;font-weight:400;font-size:4.5px}
.card-brand{left:78px;top:54px;font-size:7px}
.card-brand .brand-mark{width:7px;height:7px}
.card-contact{left:12px;top:60px;font-size:4px;line-height:6px}
.card-back .brand{position:static;font-size:13px}
.card-back .brand-mark{width:14px;height:14px}

/* envelopes */
.envelope{left:780px;width:396px}
.envelope-front{top:139px;height:185px}
.envelope-front .brand{left:18px;top:22px;font-size:13px}
.envelope-front .brand-mark{width:14px;height:14px}
.return-line{position:absolute;left:36px;top:44px;font-size:5px;color:var(--muted)}
.envelope-back{top:360px;height:168px}
.flap{position:absolute;left:0;top:0}
.flap-text{position:absolute;left:0;width:100%;top:96px;text-align:center;font-size:5px;color:var(--muted)}
</style>
</head>
<body>

<section class="piece fax-sheet">
  <div class="piece-label">Fax Sheet</div>
  <div class="brand sheet-brand"><span class="brand-mark"></span>Calibrated NET Systems</div>
  <ul class="contact sheet-contact">
    <li>T 555 014 2200</li><li>F 555 014 2201</li><li>dean.harlowe@calnet.ca</li><li>www.calnet.ca</li>
  </ul>
  <div class="fax-title">FAX</div>
  <table class="fax-table">
    <tr><td class="key">To :</td><td class="field"></td><td class="key">From :</td><td class="field"></td></tr>
    <tr><td class="key">Fax :</td><td class="field"></td><td class="key">Pages :</td><td class="field"></td></tr>
    <tr><td class="key">Phone :</td><td class="field"></td><td class="key">Date :</td><td class="field"></td></tr>
    <tr><td class="key">Re :</td><td class="field"></td><td class="key">CC :</td><td class="field"></td></tr>
  </table>
  <div class="fax-checks">
    <span>Urgent</span><span>For Review</span><span>Please Comment</span><span>Please Reply</span><span>Please Recycle</span>
  </div>
</section>

<section class="piece letterhead">
  <div class="piece-label">Letterhead</div>
  <div class="brand sheet-brand"><span class="brand-mark"></span>Calibrated NET Systems</div>
  <ul class="contact sheet-contact">
    <li>T 555 014 2200</li><li>F 555 014 2201</li><li>dean.harlowe@calnet.ca</li><li>www.calnet.ca</li>
  </ul>
</section>

<section class="piece card card-front">
  <div class="piece-label">Business Card (Front)</div>
  <svg class="card-swoosh" width="172" height="86" viewBox="0 0 172 86" aria-hidden="true">
    <path d="M0 0H172V36C120 26 60 34 0 52Z" fill="var(--blue)"/>
    <path d="M0 52C60 34 120 26 172 36V42C120 33 60 40 0 60Z" fill="var(--blue-dark)"/>
  </svg>
  <div class="card-name">Dean Harlowe<small>Technical Consultant</small></div>
  <div class="brand card-brand"><span class="brand-mark"></span>Calibrated NET</div>
  <ul class="contact card-contact">
    <li>T 555 014 2200</li><li>dean.harlowe@calnet.ca</li><li>www.calnet.ca</li>
  </ul>
</section>

<section class="piece card card-back">
  <div class="piece-label">Business Card (Back)</div>
  <div class="brand"><span class="brand-mark"></span>Calibrated NET</div>
</section>

<section class="piece envelope envelope-front">
  <div class="brand"><span class="brand-mark"></span>Calibrated NET Systems</div>
  <div class="return-line">www.calnet.ca</div>
</section>

<section class="piece envelope envelope-back">
  <div class="piece-label" style="top:-12px">Envelope (Back)</div>
  <svg class="flap" width="396" height="168" viewBox="0 0 396 168" aria-hidden="true">
    <path d="M0 0L198 92L396 0" fill="none" stroke="#c9c9c9" stroke-width="1"/>
    <path d="M0 168L160 80M396 168L236 80" fill="none" stroke="#dedede" stroke-width="1"/>
  </svg>
  <div class="flap-text">Calibrated NET Systems</div>
</section>

</body>
</html>
```